Adult Literacy Program - flyer to attract volunteers and students

We want a flyer that is engaging, colorful, modern and will appeal to our primary audience of adults aged 40-60. We are trying to attract both prospective volunteers (typically age 50+, mostly women) and students (typically aged 40+).
The flyer should feature diverse people working together in pairs of two, reading or talking, with a workbook or some reading material in front of them.

Our organization trains tutors to work one-on-one with adults who are learning how to read. Most of our adult students are non-native speakers of English. Many are of Haitian or Hispanic origin, so we would like some people who represent that demographic.

The Flyer should represent reading, learning, literacy, knowledge, growth,
and opportunities.
Our students are learning to read so they can advance their job opportunities.

Target Market(s)

Adults aged 40-60, primarily women, retired, volunteers

Industry/Entity Type

Education

Font styles to use
Serif
Sans Serif

Colors

Designer to choose colors to be used in the design.

Requirements
Must have
• - UPDATE: Should be designed as a TRI-FOLD brochure on 8.5 x 11 inch paper that will be folded into thirds.
• - Images of diverse people, women and men, who look Hispanic, Haitian and other nationalities as well as Caucasian.
• - Our logo on the front cover
Nice to have
• The sample flyer is very boring and dry! We are open to different ways of presenting the text.

```html
<!DOCTYPE html>
<html lang="en">
<head>
<meta charset="utf-8">
<title>Volunteer – Reading Bridge Friends</title>
<link href="https://fonts.googleapis.com/css2?family=Roboto+Condensed:wght@400;700&family=Varela+Round&display=swap" rel="stylesheet">
<style>
  :root {
    --paper: #ffffff;
    --sky: #83d0e1;
    --berry: #b5004f;
    --rose: #e0177a;
    --rose-soft: rgba(176, 66, 116, 0.85);
    --ink: #3a3a3a;
    --navy: #1d3f6e;
    --rule: #9a9a9a;
  }
  * { margin: 0; padding: 0; box-sizing: border-box; }
  html, body { width: 1200px; height: 865px; overflow: hidden; background: var(--paper); }
  body { font-family: "Roboto Condensed", "Arial Narrow", sans-serif; color: var(--ink); }

  .brochure { position: relative; width: 1200px; height: 865px; }

  .crop-marks { position: absolute; inset: 0; }

  /* Reply slip */
  .reply-slip { position: absolute; left: 75px; top: 88px; width: 300px; }
  .reply-title { font-size: 25px; font-weight: 700; color: var(--rose); line-height: 1; }
  .reply-role { font-size: 15px; margin-top: 12px; }
  .reply-role small { font-size: 11px; margin-left: 4px; }
  .role-option { display: flex; align-items: center; font-size: 16px; margin-top: 6px; }
  .role-option .box { width: 14px; height: 14px; border: 1.5px solid var(--rose); margin-right: 8px; }
  .fields { margin-top: 40px; }
  .field { display: flex; align-items: flex-end; height: 31px; font-size: 16px; }
  .field .label { width: 85px; }
  .field .line { flex: 1; border-bottom: 1.5px dashed var(--rule); margin-bottom: 3px; }

  .tear-line { position: absolute; left: 402px; top: 26px; height: 810px; border-left: 1px dashed var(--rule); }
  .tear-note {
    position: absolute; left: 388px; top: 400px; font-size: 10px; white-space: nowrap;
    transform: translate(-50%, -50%) rotate(90deg); transform-origin: center; margin-left: 8px;
  }

  /* Cover panels */
  .cover { position: absolute; left: 405px; top: 28px; width: 767px; height: 808px; background: var(--sky); }
  .photo { position: absolute; top: 0; height: 394px; }
  .photo-pair { left: 0; width: 381px; background: linear-gradient(160deg, #d4e3e5 0%, #a7c6cc 55%, #7fa9b1 100%); }
  .photo-tutor { left: 381px; width: 386px; background: linear-gradient(200deg, #e6e0d6 0%, #cdbfae 50%, #b5a898 100%); }
  .photo-band { position: absolute; left: 381px; top: 394px; width: 386px; height: 7px; background: var(--berry); }

  .tagline-box {
    position: absolute; left: 595px; top: 0; width: 110px; height: 160px; background: var(--rose-soft);
    color: #fff; font-family: "Varela Round", sans-serif; font-size: 21px; line-height: 1.2;
    padding: 78px 0 0 14px;
  }

  .brand { position: absolute; display: flex; flex-direction: column; align-items: center; gap: 4px;
    color: var(--navy); font-size: 12px; font-weight: 700; letter-spacing: 0.5px; text-align: center; }
  .brand .mark { width: 14px; height: 14px; background: var(--navy); }
  .brand-inside { left: 195px; top: 440px; transform: translateX(-50%); }
  .brand-back { left: 570px; top: 700px; transform: translateX(-50%); }

  .cta { position: absolute; left: 0; width: 381px; top: 522px; text-align: center; }
  .cta-title { font-size: 25px; font-weight: 700; color: var(--rose); }
  .cta-sub { font-size: 16px; color: #fff; margin-top: 2px; }

  .contact-box { position: absolute; left: 0; top: 608px; width: 381px; height: 155px; background: var(--berry);
    color: #fff; text-align: center; font-size: 16px; padding-top: 15px; line-height: 1.3; }
  .contact-box .group { margin-bottom: 8px; }
  .contact-box b { font-weight: 700; }

  .headline { position: absolute; left: 413px; top: 430px; font-family: "Varela Round", sans-serif;
    font-size: 42px; color: #fff; letter-spacing: 0.5px; }
  .mission { position: absolute; left: 413px; top: 530px; width: 300px; font-size: 19px; color: #fff; line-height: 1.2;
    font-family: Arial, Helvetica, sans-serif; }
</style>
</head>
<body>
<div class="brochure">
  <svg class="crop-marks" width="1200" height="865" aria-hidden="true">
    <g stroke="#9a9a9a" stroke-width="1">
      <line x1="0" y1="28" x2="18" y2="28"/><line x1="28" y1="0" x2="28" y2="18"/>
      <line x1="1182" y1="28" x2="1200" y2="28"/><line x1="1172" y1="0" x2="1172" y2="18"/>
      <line x1="0" y1="836" x2="18" y2="836"/><line x1="28" y1="847" x2="28" y2="865"/>
      <line x1="1182" y1="836" x2="1200" y2="836"/><line x1="1172" y1="847" x2="1172" y2="865"/>
    </g>
  </svg>

  <section class="reply-slip">
    <h2 class="reply-title">Yes, I am interested</h2>
    <p class="reply-role">in participating as: <small>(tick wherever applicable)</small></p>
    <div class="role-option"><span class="box"></span>tutor</div>
    <div class="role-option"><span class="box"></span>student</div>
    <div class="fields">
      <div class="field"><span class="label">First Name:</span><span class="line"></span></div>
      <div class="field"><span class="label">Last Name:</span><span class="line"></span></div>
      <div class="field"><span class="label">Phone:</span><span class="line"></span></div>
      <div class="field"><span class="label">Mobile:</span><span class="line"></span></div>
      <div class="field"><span class="label">email:</span><span class="line"></span></div>
    </div>
  </section>

  <div class="tear-line"></div>
  <div class="tear-note">tear along the dashed line</div>

  <section class="cover">
    <div class="photo photo-pair" role="img" aria-label="Photo of a tutor and adult learner working together at a table with a notebook"></div>
    <div class="photo photo-tutor" role="img" aria-label="Photo of a smiling volunteer tutor laughing with a learner over reading material"></div>
    <div class="photo-band"></div>
    <div class="tagline-box">Enrich<br>a Life!</div>

    <div class="brand brand-inside"><span class="mark"></span>READING BRIDGE FRIENDS</div>

    <div class="cta">
      <p class="cta-title">Don’t waste a moment!</p>
      <p class="cta-sub">Contact us today to learn more.</p>
    </div>

    <div class="contact-box">
      <div class="group"><b>Volunteer Desk:</b><br>555-210-4830</div>
      <div class="group"><b>Cedar Hollow, Millbrook &amp; East Point:</b><br>555-376-9142</div>
      <div class="group"><b>email:</b> hello@readingbridge.org</div>
    </div>

    <h1 class="headline">VOLUNTEER</h1>
    <p class="mission">Help an adult learn to read, write or speak English.</p>

    <div class="brand brand-back"><span class="mark"></span>READING BRIDGE FRIENDS</div>
  </section>
</div>
</body>
</html>
```